“Fleet Vehicle Branding: Truck Wrap for Brightline Heating & Air”

The C in custom must be the same as in the logo tan and blue image
the logo .jpg need to have that same C. are colors are Tan and navy blue not sure how we weather we want most the truck tan or blue with some of these things from logos. also are saying is brightline warmth brightline service brightline heating and air. we would like to stand out from traditional hvac wrap looks

Target Market(s)

Residential Customers

Industry/Entity Type

Hvac

Colors

Designer to choose colors to be used in the design.

Requirements
Must have
• TACLB118356K
Nice to have
• www.brightlineheating-air.example

```html
<!DOCTYPE html>
<html lang="en">
<head>
<meta charset="utf-8">
<title>Brightline Heating &amp; Air – Fleet Van Wrap</title>
<link rel="stylesheet" href="https://fonts.googleapis.com/css2?family=Oswald:wght@500;600&family=Montserrat:ital,wght@0,600;0,700;1,600;1,700&display=swap">
<style>
  :root{
    --navy:#1d2d57;
    --navy-deep:#16244a;
    --tan:#c8b28b;
    --tan-light:#dccbab;
    --tan-text:#b9a27a;
    --white:#f4f4f4;
    --body-grey:#e2e3e5;
    --rocker:#3b3e45;
    --tyre:#26272b;
    --hub:#b9bcc1;
    --glass:#2b3038;
    --page:#ffffff;
  }
  html,body{margin:0;padding:0;overflow:hidden;background:var(--page);}
  .canvas{position:relative;width:1200px;height:2882px;overflow:hidden;background:var(--page);}
  .view{position:absolute;left:0;width:1200px;display:block;}
  .view--front{top:0;height:800px;}
  .view--driver{top:840px;height:520px;}
  .view--passenger{top:1430px;height:520px;}
  .view--rear{top:2010px;height:860px;}
  .brand{font-family:"Oswald",sans-serif;font-weight:600;fill:var(--tan-text);}
  .brand--navy{fill:var(--navy);}
  .tagline{font-family:"Montserrat",sans-serif;font-weight:600;fill:var(--tan-light);}
  .tagline--light{fill:var(--white);}
  .licence{font-family:"Montserrat",sans-serif;font-weight:700;font-style:italic;fill:var(--navy);}
  .licence--light{fill:var(--white);}
  .phone{font-family:"Oswald",sans-serif;font-weight:500;fill:var(--navy);letter-spacing:1px;}
  .services{font-family:"Montserrat",sans-serif;font-weight:600;font-style:italic;fill:var(--navy);}
  .web{font-family:"Montserrat",sans-serif;font-weight:700;font-style:italic;fill:var(--navy);}
  .web--front{font-style:normal;}
  .web--rear{font-style:normal;fill:var(--tan-light);letter-spacing:3px;font-weight:600;}
  .service-list{font-family:"Montserrat",sans-serif;font-weight:700;fill:var(--white);}
  .mascot{fill:url(#mascotTone);stroke:#2a2c31;stroke-width:3;}
</style>
</head>
<body>
<div class="canvas">

  <svg width="0" height="0" style="position:absolute">
    <defs>
      <linearGradient id="wrapFade" x1="0" y1="0" x2="0" y2="1">
        <stop offset="0" stop-color="#1d2d57"/>
        <stop offset=".45" stop-color="#4f5668"/>
        <stop offset=".8" stop-color="#c8b28b"/>
        <stop offset="1" stop-color="#dccbab"/>
      </linearGradient>
      <linearGradient id="mascotTone" x1="0" y1="0" x2="1" y2="1">
        <stop offset="0" stop-color="#c9ccd1"/>
        <stop offset="1" stop-color="#8d9199"/>
      </linearGradient>
    </defs>
  </svg>

  <!-- Front view -->
  <svg class="view view--front" viewBox="0 0 1200 800" aria-label="Van wrap, front view">
    <path d="M330,70 Q340,40 420,36 L780,36 Q860,40 870,70 L920,420 L930,560 Q930,600 900,610 L300,610 Q270,600 270,560 L280,420 Z" fill="var(--body-grey)"/>
    <path d="M345,125 Q355,112 380,112 L820,112 Q845,112 855,125 L880,300 L320,300 Z" fill="var(--glass)"/>
    <rect x="205" y="255" width="70" height="120" rx="18" fill="var(--tyre)"/>
    <rect x="925" y="255" width="70" height="120" rx="18" fill="var(--tyre)"/>
    <path d="M280,360 L390,375 L380,440 L290,430 Z" fill="#cfd2d6" stroke="#8d9096" stroke-width="3"/>
    <path d="M920,360 L810,375 L820,440 L910,430 Z" fill="#cfd2d6" stroke="#8d9096" stroke-width="3"/>
    <rect x="405" y="380" width="390" height="135" rx="40" fill="#2c2f35" stroke="#b7bbc1" stroke-width="10"/>
    <g stroke="#b7bbc1" stroke-width="7">
      <line x1="425" y1="412" x2="775" y2="412"/>
      <line x1="420" y1="447" x2="780" y2="447"/>
      <line x1="425" y1="482" x2="775" y2="482"/>
    </g>
    <path d="M260,510 L940,510 L950,640 Q950,670 920,675 L280,675 Q250,670 250,640 Z" fill="#5c5f66"/>
    <rect x="430" y="600" width="340" height="45" rx="8" fill="#34373d"/>
    <rect x="262" y="640" width="90" height="130" rx="20" fill="var(--tyre)"/>
    <rect x="848" y="640" width="90" height="130" rx="20" fill="var(--tyre)"/>
    <text class="web web--front" x="600" y="100" text-anchor="middle" font-size="22">www.brightlineheating-air.example</text>
    <text class="brand brand--navy" x="600" y="338" text-anchor="middle" font-size="30">Brightline</text>
    <text class="brand brand--navy" x="600" y="356" text-anchor="middle" font-size="12" letter-spacing="1">HEATING &amp; AIR CONDITIONING</text>
  </svg>

  <!-- Driver side -->
  <svg class="view view--driver" viewBox="0 0 1200 520" aria-label="Van wrap, left side">
    <defs>
      <clipPath id="bodyLeft">
        <path d="M45,30 Q45,18 62,18 L740,18 Q800,20 835,62 L1000,200 Q1100,222 1168,250 Q1185,262 1185,300 L1185,400 L45,400 Z"/>
      </clipPath>
    </defs>
    <path d="M45,30 Q45,18 62,18 L740,18 Q800,20 835,62 L1000,200 Q1100,222 1168,250 Q1185,262 1185,300 L1185,400 L45,400 Z" fill="var(--white)"/>
    <g clip-path="url(#bodyLeft)">
      <path d="M45,18 L555,18 L700,330 L45,330 Z" fill="url(#wrapFade)"/>
      <path d="M640,215 L710,330 L745,330 Z" fill="var(--navy)"/>
      <rect x="40" y="330" width="1150" height="75" fill="var(--rocker)"/>
      <path d="M340,360 L700,360 L715,385 L345,385 Z" fill="var(--tan)"/>
      <path d="M700,360 L720,360 L740,385 L715,385 Z" fill="var(--navy)"/>
      <path d="M720,360 L900,360 L900,385 L740,385 Z" fill="var(--white)"/>
    </g>
    <path d="M770,85 Q775,72 790,76 L925,185 L925,230 L775,230 Z" fill="var(--glass)"/>
    <path d="M935,190 L990,210 L985,240 L935,235 Z" fill="var(--glass)"/>
    <path d="M1130,255 L1180,270 L1178,300 L1135,290 Z" fill="#e6a23c"/>
    <rect x="40" y="180" width="14" height="70" rx="3" fill="#b3262a"/>
    <circle cx="245" cy="430" r="72" fill="var(--tyre)"/><circle cx="245" cy="430" r="40" fill="var(--hub)"/>
    <circle cx="1040" cy="430" r="72" fill="var(--tyre)"/><circle cx="1040" cy="430" r="40" fill="var(--hub)"/>
    <text class="tagline" x="72" y="46" font-size="11.5" textLength="465" lengthAdjust="spacingAndGlyphs">BRIGHTLINE WARMTH | BRIGHTLINE SERVICE | BRIGHTLINE HEATING AND AIR</text>
    <text class="licence" x="590" y="50" font-size="19">TACLB118356K</text>
    <text class="brand" x="178" y="128" font-size="62">Brightline</text>
    <text class="brand" x="178" y="178" font-size="36">HEATING &amp;</text>
    <text class="brand" x="180" y="210" font-size="24">AIR CONDITIONING</text>
    <line x1="140" y1="228" x2="440" y2="228" stroke="var(--navy-deep)" stroke-width="4"/>
    <path d="M178,244 q-8,8 0,18 l5,4 q4,2 7,-2 l-5,-6 -4,2 q-3,-4 0,-9 l4,2 4,-6 z" fill="var(--white)"/>
    <text class="phone" x="198" y="264" font-size="25">972-555-0148</text>
    <text class="services" x="75" y="288" font-size="12">• HEATING  • COOLING  • MAINTENANCE  • INSTALLATION</text>
    <rect class="mascot" x="455" y="60" width="190" height="245" rx="22" role="img" aria-label="Cartoon outdoor air-conditioner unit mascot"/>
    <text class="web" transform="translate(823,272) rotate(4)" font-size="15">www.brightlineheating-air.example</text>
  </svg>

  <!-- Passenger side -->
  <svg class="view view--passenger" viewBox="0 0 1200 520" aria-label="Van wrap, right side">
    <defs>
      <clipPath id="bodyRight">
        <path transform="translate(1200,0) scale(-1,1)" d="M45,30 Q45,18 62,18 L740,18 Q800,20 835,62 L1000,200 Q1100,222 1168,250 Q1185,262 1185,300 L1185,400 L45,400 Z"/>
      </clipPath>
    </defs>
    <path transform="translate(1200,0) scale(-1,1)" d="M45,30 Q45,18 62,18 L740,18 Q800,20 835,62 L1000,200 Q1100,222 1168,250 Q1185,262 1185,300 L1185,400 L45,400 Z" fill="var(--white)"/>
    <g clip-path="url(#bodyRight)">
      <path d="M1155,18 L645,18 L500,330 L1155,330 Z" fill="url(#wrapFade)"/>
      <path d="M560,215 L490,330 L455,330 Z" fill="var(--navy)"/>
      <rect x="10" y="330" width="1150" height="75" fill="var(--rocker)"/>
      <path d="M860,360 L500,360 L485,385 L855,385 Z" fill="var(--tan)"/>
      <path d="M500,360 L480,360 L460,385 L485,385 Z" fill="var(--navy)"/>
      <path d="M480,360 L300,360 L300,385 L460,385 Z" fill="var(--white)"/>
    </g>
    <path d="M430,85 Q425,72 410,76 L275,185 L275,225 L425,225 Z" fill="var(--glass)"/>
    <path d="M265,190 L210,208 L214,232 L265,228 Z" fill="var(--glass)"/>
    <path d="M70,255 L20,270 L22,300 L65,290 Z" fill="#e6a23c"/>
    <rect x="1146" y="180" width="14" height="70" rx="3" fill="#b3262a"/>
    <circle cx="160" cy="430" r="72" fill="var(--tyre)"/><circle cx="160" cy="430" r="40" fill="var(--hub)"/>
    <circle cx="955" cy="430" r="72" fill="var(--tyre)"/><circle cx="955" cy="430" r="40" fill="var(--hub)"/>
    <text class="tagline" x="1128" y="46" font-size="11.5" text-anchor="end" textLength="465" lengthAdjust="spacingAndGlyphs">BRIGHTLINE WARMTH | BRIGHTLINE SERVICE | BRIGHTLINE HEATING AND AIR</text>
    <text class="licence" x="440" y="50" font-size="19">TACLB118356K</text>
    <text class="brand" x="828" y="128" font-size="62">Brightline</text>
    <text class="brand" x="828" y="178" font-size="36">HEATING &amp;</text>
    <text class="brand" x="830" y="210" font-size="24">AIR CONDITIONING</text>
    <path d="M848,244 q-8,8 0,18 l5,4 q4,2 7,-2 l-5,-6 -4,2 q-3,-4 0,-9 l4,2 4,-6 z" fill="var(--white)"/>
    <text class="phone" x="868" y="264" font-size="25">972-555-0148</text>
    <text class="services" x="1125" y="288" font-size="12" text-anchor="end">• HEATING  • COOLING  • MAINTENANCE  • INSTALLATION</text>
    <rect class="mascot" x="555" y="60" width="190" height="245" rx="22" role="img" aria-label="Cartoon outdoor air-conditioner unit mascot"/>
    <text class="web" transform="translate(125,282) rotate(-5)" font-size="15">www.brightlineheating-air.example</text>
  </svg>

  <!-- Rear view -->
  <svg class="view view--rear" viewBox="0 0 1200 860" aria-label="Van wrap, rear view">
    <path d="M300,40 Q310,20 360,18 L840,18 Q890,20 900,40 L930,200 L930,720 L270,720 L270,200 Z" fill="url(#wrapFade)"/>
    <line x1="600" y1="25" x2="600" y2="720" stroke="#101a33" stroke-width="3"/>
    <rect x="560" y="5" width="80" height="12" rx="4" fill="#8a1f22"/>
    <rect x="262" y="390" width="30" height="260" rx="6" fill="#b3262a"/>
    <rect x="908" y="390" width="30" height="260" rx="6" fill="#b3262a"/>
    <rect x="632" y="535" width="72" height="16" rx="6" fill="#2c2f35"/>
    <path d="M250,720 L950,720 L955,800 Q955,825 925,828 L275,828 Q245,825 245,800 Z" fill="var(--rocker)"/>
    <rect x="280" y="828" width="90" height="30" rx="8" fill="var(--tyre)"/>
    <rect x="830" y="828" width="90" height="30" rx="8" fill="var(--tyre)"/>
    <text class="web web--rear" x="600" y="68" text-anchor="middle" font-size="24">www.brightlineheating-air.example</text>
    <text class="brand" x="320" y="210" font-size="72" textLength="300" lengthAdjust="spacingAndGlyphs">Brightline</text>
    <text class="brand" x="320" y="288" font-size="54">HEATING &amp;</text>
    <text class="brand" x="322" y="330" font-size="36">AIR CONDITIONING</text>
    <rect class="mascot" x="650" y="115" width="165" height="225" rx="22" role="img" aria-label="Cartoon outdoor air-conditioner unit mascot"/>
    <text class="tagline tagline--light" x="600" y="380" text-anchor="middle" font-size="13.5" letter-spacing=".6">BRIGHTLINE WARMTH | BRIGHTLINE SERVICE | BRIGHTLINE HEATING AND AIR</text>
    <g class="service-list" font-size="22">
      <circle cx="370" cy="490" r="5" fill="var(--navy)"/><text x="383" y="498">HEATING</text>
      <circle cx="370" cy="521" r="5" fill="var(--navy)"/><text x="383" y="529">COOLING</text>
      <circle cx="370" cy="552" r="5" fill="var(--navy)"/><text x="383" y="560">MAINTENANCE</text>
      <circle cx="370" cy="583" r="5" fill="var(--navy)"/><text x="383" y="591">INSTALLATION</text>
    </g>
    <text class="licence licence--light" x="745" y="582" text-anchor="middle" font-size="29">TACLB118356K</text>
  </svg>

</div>
</body>
</html>
```